Banner Pop Up Opt In Form REDESIGNS - SLEEK BLACK LOOK

Please redesign banners attached.

I am looking for a very sleek look....I do not like this collage of images on these current designs. Please keep all content same but use images that pop.

I have an acccount at www.pixmorrow-example.com or you can use your own images.

I like black background for somereason because it looks very sleek....but these designs should pop , build trust and credibility and have easy opt in form....SLEEK AND MODERN LOOK is what im looking for....

Target Market(s)

Consumers on websites

Requirements
Must have
• Please redesign banners attached.

Nice to have

Should not have

```html
<!DOCTYPE html>
<html lang="en">
<head>
<meta charset="utf-8">
<title>Newsletter Opt-In Banners</title>
<link rel="stylesheet" href="https://fonts.googleapis.com/css2?family=Playfair+Display:wght@700&family=Montserrat:wght@400;500;700&display=swap">
<style>
:root{
  --page:#000000;
  --orange:#f3a24c;
  --espresso:#2a1d14;
  --cream:#ffffff;
  --slate:#1f2226;
  --muted:#c9ccd0;
}
*{margin:0;padding:0;box-sizing:border-box}
html,body{width:1200px;height:2400px;overflow:hidden;background:var(--page)}
body{position:relative;font-family:"Montserrat",Arial,sans-serif}

.banner{position:absolute;left:120px;width:960px;height:960px;overflow:hidden}
.banner--offer{top:142px}
.banner--contest{top:1300px;background:var(--slate)}

.photo{position:absolute;left:0;width:960px}
.photo--friends{top:0;height:924px;
  background:linear-gradient(180deg,#2c2016 0%,#3a2a1c 30%,#7a5432 52%,#b98455 66%,#3f7f9a 78%,#bfe0ee 86%,#e8f3f8 100%)}
.photo--villa{top:0;height:536px;
  background:linear-gradient(180deg,#aab9c8 0%,#d8dde2 25%,#c9b8a0 48%,#8a6a4c 68%,#5fb9d0 78%,#6e5039 90%,#4a3526 100%)}
.backdrop--contest{position:absolute;left:0;top:536px;width:960px;height:424px;
  background:linear-gradient(180deg,#26292e 0%,#1c1f23 60%,#202428 100%)}

.headline{position:absolute;font-family:"Playfair Display",Georgia,serif;font-weight:700;
  color:var(--orange);font-size:66px;line-height:1;letter-spacing:-2px;white-space:nowrap}
.banner--offer .headline{left:0;width:960px;text-align:center;top:46px}
.banner--contest .headline{left:28px;top:586px}

.intro{position:absolute;color:var(--cream);font-weight:500;font-size:23px;
  letter-spacing:4px;line-height:37px;text-transform:uppercase}
.banner--offer .intro{left:0;width:960px;text-align:center;top:124px}
.banner--contest .intro{left:28px;top:677px;font-size:24px}

.ribbon{position:absolute}
.banner--offer .ribbon{left:213px;top:216px;width:533px;height:74px}
.banner--contest .ribbon{left:0;top:791px;width:444px;height:66px}
.ribbon svg{position:absolute;left:0;top:0}
.ribbon__text{position:absolute;color:var(--espresso);font-weight:700;
  font-size:24px;letter-spacing:4.5px;line-height:33px;text-transform:uppercase}
.banner--offer .ribbon__text{left:0;width:533px;text-align:center;top:4px}
.banner--contest .ribbon__text{left:28px;top:1px;font-size:23px;line-height:30px}

.field{position:absolute;height:40px;border-bottom:2px solid var(--espresso);
  text-align:center;font-size:21px;letter-spacing:3px;color:#3b3b3b;line-height:36px}
.banner--contest .field{border-color:var(--cream);color:var(--muted)}
.submit{position:absolute;font-weight:700;font-size:21px;letter-spacing:4px;
  text-align:center;line-height:50px;height:50px}
.banner--offer .submit{background:var(--espresso);color:var(--orange)}
.banner--contest .submit{background:var(--orange);color:var(--espresso)}

.note{position:absolute;left:0;width:960px;text-align:center;font-size:15.5px;
  letter-spacing:0.2px;text-transform:uppercase}
.banner--offer .note{top:924px;height:36px;line-height:36px;background:var(--orange);color:var(--espresso)}
.banner--contest .note{top:930px;color:var(--muted)}
</style>
</head>
<body>

<section class="banner banner--offer">
  <div class="photo photo--friends" role="img" aria-label="Friends in sunglasses laughing together in a resort pool"></div>
  <h1 class="headline">WANT A GREAT OFFER?</h1>
  <p class="intro">Subscribe to our newsletter and<br>receive a complimentary</p>
  <div class="ribbon">
    <svg width="533" height="74" viewBox="0 0 533 74">
      <polygon points="0,0 533,0 503,74 0,74" fill="var(--orange)"/>
      <polygon points="0,0 32,0 16,36" fill="var(--cream)"/>
      <polygon points="503,74 533,74 521,38" fill="var(--cream)"/>
    </svg>
    <p class="ribbon__text">7 Night Resort/Condo-<br>3500 + Locations</p>
  </div>
  <form>
    <div class="field" style="left:52px;top:786px;width:392px">NAME</div>
    <div class="field" style="left:517px;top:786px;width:393px">EMAIL</div>
    <div class="field" style="left:52px;top:855px;width:392px">PHONE</div>
    <div class="submit" style="left:517px;top:845px;width:393px">SUBMIT</div>
  </form>
  <p class="note">We will send an email and a text message with the offer and instructions on how to redeem.</p>
</section>

<section class="banner banner--contest">
  <div class="photo photo--villa" role="img" aria-label="Modern villa terrace with lounge chairs and a blue pool at dusk"></div>
  <div class="backdrop--contest"></div>
  <h2 class="headline">ENTER TO WIN</h2>
  <p class="intro">Subscribe to our newsletter<br>to enter to win a</p>
  <div class="ribbon">
    <svg width="444" height="66" viewBox="0 0 444 66">
      <polygon points="0,0 444,0 418,66 0,66" fill="var(--orange)"/>
      <polygon points="418,66 444,66 432,34" fill="var(--cream)"/>
    </svg>
    <p class="ribbon__text">7 Night Resort/Condo-<br>3500 + Locations</p>
  </div>
  <form>
    <div class="field" style="left:604px;top:586px;width:306px">NAME</div>
    <div class="field" style="left:604px;top:657px;width:306px">EMAIL</div>
    <div class="field" style="left:604px;top:728px;width:306px">PHONE</div>
    <div class="submit" style="left:604px;top:806px;width:306px">SUBMIT</div>
  </form>
  <p class="note">We will send an email and a text message with the offer and instructions on how to redeem.</p>
</section>

</body>
</html>
```